Private Villa in Bali looking for a flyer design

We need a flyer design for a 2bedrooms private villa with pool in Bali, called VILLA TESKA

Our villa is a private 2 bedrooms villa with private swimming pool, tranquil , luxurious, blending balinese and modern interiors , personal service and family home away from home
Out Motto : your blissful getaway

We would like an elegant, luxury and clean design

Colour scheme : BROWN, YELLOW/GOLD, GREY

It should have :
1/photo of the villa
2/ basic info of the villa
3/ location/address and location map of the villa

Villa Teska
Banjar Kelodsari,
Pererenan, Canggu
Bali - Indonesia

4/ website :
www.villateskamora

5/ email :
wulan@villateskamora.com

6/ Phone :
+852-47290516

I have attached some photos and the logo, please let me know if you need ai/eps file

Thank you . Please let me know if you need more information
Updates

-Trifold flyer on A4 size paper ( standard size flyer)

-Front page : Main photo and Logo
-Last page : Location map, email,website etc
-Page 2-4 : any design with photo and info from website 

Target Market(s)

Family, couples, honeymooners

Industry/Entity Type

It Service

Colors
ffc214
474747
9d9d9d

Requirements
Must have
• address, location map, website and email add, photos ( don't need to use all)

Trifold on A4 size paper double sided
Nice to have
• Trifold on A4 size paper
Should not have
• too many photos overlapping .

```html
<!DOCTYPE html>
<html lang="en">
<head>
<meta charset="utf-8">
<title>Villa Teska – Trifold Flyer</title>
<link href="https://fonts.googleapis.com/css2?family=Dancing+Script:wght@500&family=Raleway:wght@400;500&display=swap" rel="stylesheet">
<style>
  :root {
    --paper: #f2f2f1;
    --brown-dark: #3b2612;
    --brown-mid: #5b3b1d;
    --gold: #c9a24a;
    --gold-soft: #d8b872;
    --yellow: #ffc214;
    --ink: #474747;
    --ink-soft: #5c5c5c;
    --grey: #9d9d9d;
  }
  * { box-sizing: border-box; margin: 0; padding: 0; }
  html, body { width: 1200px; height: 848px; overflow: hidden; background: #fff; }
  .flyer {
    position: relative;
    width: 1200px;
    height: 848px;
    font-family: "Raleway", Arial, sans-serif;
    color: var(--ink);
    background: var(--paper);
  }
  .panel { position: absolute; width: 400px; }
  .row-top .panel { top: 0; height: 331px; }
  .row-bottom .panel { top: 542px; height: 306px; }
  .col-1 { left: 0; }
  .col-2 { left: 400px; }
  .col-3 { left: 800px; }

  .photo-pool { background: linear-gradient(180deg, #3c5fa8 0%, #6d5a4a 40%, #2f9fe0 62%, #1a6fd0 100%); }
  .photo-dining { background: linear-gradient(120deg, #b88a4e 0%, #c4261b 45%, #4a2418 100%); }
  .photo-lounge { background: linear-gradient(160deg, #7a3e1a 0%, #e0962e 40%, #a8321e 70%, #3a2214 100%); }

  .contact {
    background: var(--paper);
    text-align: center;
  }
  .contact-info { padding-top: 34px; height: 160px; font-size: 11px; line-height: 14px; }
  .contact-info .place { color: var(--ink); font-weight: 500; margin-bottom: 8px; }
  .contact-info .links { color: var(--ink-soft); }
  .contact-info .rule { display: block; margin: 14px auto 0; }
  .map { position: absolute; left: 0; top: 160px; width: 400px; height: 171px; background: linear-gradient(180deg, #f4f4f4, #e4e4e4); }

  .gold-line { position: absolute; left: 0; width: 1200px; height: 3px; background: var(--gold); }
  .gold-line.upper { top: 331px; }
  .gold-line.lower { top: 537px; }
  .brand-band {
    position: absolute; left: 0; top: 334px; width: 1200px; height: 203px;
    background: linear-gradient(180deg, var(--brown-mid) 0%, var(--brown-dark) 100%);
  }
  .brand {
    position: absolute; left: 120px; top: 54px; width: 160px; text-align: center;
  }
  .brand-square { display: block; width: 60px; height: 60px; margin: 0 auto 12px; background: var(--yellow); }
  .brand-name { font-size: 22px; font-weight: 400; color: var(--gold-soft); letter-spacing: 0.5px; }

  .getaway { text-align: center; background: var(--paper); }
  .getaway .rule { display: block; margin: 88px auto 0; }
  .getaway h2 {
    font-family: "Dancing Script", cursive;
    font-weight: 500; font-size: 34px; color: var(--brown-dark);
    margin-top: 22px;
  }
  .getaway .tagline { font-size: 11px; line-height: 14px; color: var(--ink-soft); margin: 4px auto 0; width: 260px; }
  .getaway .site { position: absolute; left: 0; right: 0; bottom: 16px; font-size: 12px; letter-spacing: 1.5px; color: var(--ink); }

  .welcome { text-align: center; background: var(--paper); padding: 50px 26px 0; }
  .welcome h2 {
    font-family: "Dancing Script", cursive;
    font-weight: 500; font-size: 34px; color: var(--brown-dark);
  }
  .welcome p { margin-top: 14px; font-size: 11.6px; line-height: 17.5px; color: var(--ink); }
  .welcome .rule { display: block; margin: 18px auto 0; }
</style>
</head>
<body>
<main class="flyer">
  <section class="row-top">
    <div class="panel col-1 photo-pool" role="img" aria-label="Photo of the villa pool and pavilion at dusk"></div>
    <div class="panel col-2 contact">
      <div class="contact-info">
        <p class="place">Villa Teska is located in<br>a beautiful area of Pererenan - Canggu<br>Bali - Indonesia</p>
        <p class="links">enquiry@villateskamora.com<br>www.villateskamora.com</p>
        <svg class="rule" width="60" height="8" viewBox="0 0 60 8"><line x1="0" y1="4" x2="60" y2="4" stroke="#c9a24a" stroke-width="1"/></svg>
      </div>
      <div class="map" role="img" aria-label="Location map of Pererenan and Canggu with a pin marking the villa"></div>
    </div>
    <div class="panel col-3 photo-dining" role="img" aria-label="Photo of the dining and living room with red walls"></div>
  </section>

  <div class="gold-line upper"></div>
  <section class="brand-band">
    <div class="brand">
      <span class="brand-square"></span>
      <span class="brand-name">Villa Teska</span>
    </div>
  </section>
  <div class="gold-line lower"></div>

  <section class="row-bottom">
    <div class="panel col-1 getaway">
      <svg class="rule" width="60" height="8" viewBox="0 0 60 8"><line x1="0" y1="4" x2="60" y2="4" stroke="#c9a24a" stroke-width="1"/></svg>
      <h2>Your blissful Getaway</h2>
      <p class="tagline">A stylish blend of classic Balinese architecture mixed with contemporary design.</p>
      <p class="site">www.villateskamora.com</p>
    </div>
    <div class="panel col-2 photo-lounge" role="img" aria-label="Photo of the lounge with sofa, cushions and high timber ceiling"></div>
    <div class="panel col-3 welcome">
      <h2>Welcome to Villa Teska</h2>
      <p>Since the beginning of time Bali has been known as the ‘Island of the Gods’ a mystical and beautiful place that has captured the hearts and imaginations of all who lay eyes on her. Away from the hustle and bustle of the modern world, yet close enough to the conveniences that make life comfortable Villa Teska is nestled in the charming Balinese village of Pererenan, Canggu.</p>
      <svg class="rule" width="60" height="8" viewBox="0 0 60 8"><line x1="0" y1="4" x2="60" y2="4" stroke="#c9a24a" stroke-width="1"/></svg>
    </div>
  </section>
</main>
</body>
</html>
```